A Responsive Wordpress Template Design.

The old site http://harbourframe.co.nz/ is now looking outdated.

The Home Page should be designed to quickly get the visitor to the sales / landing pages:

Chalet, Duplex, Annex, Traveller, Residential and Business.

The navigation should be by a Navigation Bar under the Header.

The main page should be divided into boxes with one for each of the landing pages (Chalet, Duplex, Annex... etc.). In a similar way to this site: http://boomdeckhire.co.nz/

The logo should remain as is. The colors should be based on the logo.

The client does not like the modern trend of big graphics across the page.

Target Market(s)

General public, home buyers

Industry/Entity Type

Sales

Number of Pages Required

2 page

Font styles to use
Sans Serif

Requirements
Must have
• See brief
Nice to have
• See brief
Should not have
• See brief

```html
<!DOCTYPE html>
<html lang="en">
<head>
<meta charset="utf-8">
<title>Harbourframe – Relocatable Holiday Homes</title>
<link href="https://fonts.googleapis.com/css2?family=Arimo:wght@400;700&family=Open+Sans:ital,wght@0,400;0,600;0,700;1,400;1,600&display=swap" rel="stylesheet">
<style>
:root{
  --blue:#1f4f8f;
  --navy:#1b3d6e;
  --dark:#242021;
  --text:#555;
  --heading:#333;
  --band:#efefef;
  --line:#e2e2e2;
  --white:#fff;
}
*{box-sizing:border-box;margin:0;padding:0}
html,body{width:774px;height:1200px;overflow:hidden;background:var(--white)}
body{position:relative;font-family:"Open Sans",sans-serif;color:var(--text)}
.abs{position:absolute}
a{color:inherit}

/* header */
.brand{left:64px;top:30px;display:flex;align-items:center;gap:6px}
.brand-mark{width:12px;height:12px;background:var(--navy)}
.brand-name{font-family:"Arimo",sans-serif;font-weight:700;font-size:16px;color:var(--dark);letter-spacing:.5px}
.contact-item{top:20px;display:flex;align-items:center;gap:10px;font-size:11px}
.contact-icon{width:28px;height:28px;border-radius:50%;background:var(--navy);display:flex;align-items:center;justify-content:center}
.phone-text{font-family:"Arimo",sans-serif;font-weight:700;color:#444}
.mail-text{color:#444;text-decoration:underline}

/* nav */
.nav{left:0;top:68px;width:774px;height:32px;background:var(--dark)}
.nav-active{left:64px;top:0;width:76px;height:32px;background:var(--blue);clip-path:polygon(0 0,100% 0,82% 100%,0 100%)}
.nav-item{top:11px;font-family:"Arimo",sans-serif;font-weight:700;font-size:8.5px;color:var(--white);letter-spacing:.2px}

/* hero, kept inside the content width */
.hero{left:64px;top:112px;width:646px;height:220px;background:linear-gradient(90deg,#4f5a36 0%,#7d8a55 28%,#c7c9c3 55%,#dcdedc 75%,#6b7a4a 100%)}
.hero-title{left:64px;top:210px;width:646px;text-align:center;font-family:"Arimo",sans-serif;font-weight:700;font-size:22px;color:var(--white);text-shadow:0 1px 3px rgba(0,0,0,.5);letter-spacing:.5px}
.hero-dots{left:358px;top:312px;display:flex;gap:5px}
.hero-dots span{width:9px;height:9px;border-radius:50%;border:1.5px solid var(--white)}
.hero-dots span:first-child{background:var(--white)}

/* welcome */
.welcome-title{left:64px;top:369px;font-family:"Arimo",sans-serif;font-weight:700;font-size:13px;color:var(--heading)}
.welcome-sub{left:64px;top:390px;font-style:italic;font-weight:600;font-size:9.5px;color:var(--navy)}
.welcome-copy{left:64px;top:415px;width:462px;font-size:7.6px;line-height:14px}
.welcome-copy p+p{margin-top:9px}
.read-more{left:64px;top:516px;font-family:"Arimo",sans-serif;font-weight:700;font-size:7.5px;color:var(--navy);text-decoration:none}
.badge{left:568px;top:380px}

/* range boxes linking to landing pages */
.range{left:0;top:549px;width:774px;height:198px;background:var(--band)}
.range-title{left:0;top:22px;width:774px;text-align:center;font-family:"Arimo",sans-serif;font-weight:700;font-size:12.5px;color:#555}
.range-card{top:58px;width:99px;height:118px;background:var(--white);border:1px solid #ddd;text-decoration:none}
.range-photo{position:absolute;left:3px;top:3px;width:91px;height:72px}
.range-name{position:absolute;left:0;top:81px;width:97px;text-align:center;font-family:"Arimo",sans-serif;font-weight:700;font-size:9px;color:var(--heading)}
.range-more{position:absolute;left:0;top:98px;width:97px;text-align:center;font-family:"Arimo",sans-serif;font-weight:700;font-size:7px;color:var(--navy)}

/* boxes */
.box{top:773px;height:222px;background:#f7f7f7;border:2px solid #e6e6e6}
.box-title{position:absolute;left:10px;right:10px;top:12px;padding-bottom:10px;border-bottom:1px solid var(--line);font-family:"Arimo",sans-serif;font-weight:700;font-size:12px;color:#444}
.quote{position:absolute;left:12px;top:52px;width:185px;font-style:italic;font-size:8.2px;line-height:19px;color:#777}
.quote b{color:var(--navy);font-style:normal;font-size:11px}
.quote-author{position:absolute;left:12px;top:162px;font-size:8px;color:#777;font-style:italic}
.quote-author strong{font-style:normal;font-family:"Arimo",sans-serif;font-size:8.5px;color:var(--navy)}
.news{position:absolute;left:10px;width:176px;padding-bottom:9px;border-bottom:1px solid var(--line)}
.news-title{font-family:"Arimo",sans-serif;font-size:8.2px;color:#333;padding-left:16px;position:relative}
.news-title:before{content:"";position:absolute;left:0;top:4px;width:9px;height:1.5px;background:var(--navy)}
.news-meta{margin-top:5px;padding-left:18px;font-style:italic;font-size:7px;color:var(--navy);display:flex;gap:10px}
.box-link{position:absolute;bottom:18px;font-family:"Arimo",sans-serif;font-weight:700;font-size:7.5px;color:var(--navy);text-decoration:none}
.map{position:absolute;left:1px;top:35px;width:201px;height:146px;background:linear-gradient(135deg,#ece6d8 0%,#e4dfd2 55%,#a9c7e8 75%,#9cc0e6 100%)}

/* footer */
.footer{left:0;top:1025px;width:774px;height:175px;background:var(--dark);color:#ddd}
.foot-head{top:21px;font-family:"Arimo",sans-serif;font-weight:700;font-size:10.5px;color:var(--white)}
.foot-links{top:45px;display:flex;flex-direction:column;gap:7.5px;font-size:7.4px}
.foot-links a{text-decoration:underline;color:#ddd}
.foot-contact{left:433px;top:49px;display:flex;flex-direction:column;gap:5.5px;font-size:7.4px}
.foot-contact div{display:flex;gap:8px;align-items:flex-start}
.foot-contact svg{flex:none;margin-top:1px}
.foot-brand{left:596px;top:70px;display:flex;align-items:center;gap:6px}
.foot-brand .brand-mark{background:var(--white);width:11px;height:11px}
.foot-brand .brand-name{color:var(--white);font-size:13.5px}
.copyright{left:64px;top:149px;font-size:7.5px}
.social{left:620px;top:145px;display:flex;gap:4px}
.social span{width:20px;height:20px;border-radius:50%;border:1.5px solid var(--white)}
</style>
</head>
<body>

<header>
  <div class="abs brand"><span class="brand-mark"></span><span class="brand-name">HARBOURFRAME</span></div>
  <div class="abs contact-item" style="left:430px">
    <span class="contact-icon"><svg width="13" height="13" viewBox="0 0 24 24"><path fill="#fff" d="M6.6 10.8a15 15 0 0 0 6.6 6.6l2.2-2.2c.3-.3.7-.4 1-.2 1.1.4 2.3.6 3.6.6.6 0 1 .4 1 1V20c0 .6-.4 1-1 1A17 17 0 0 1 3 4c0-.6.4-1 1-1h3.5c.6 0 1 .4 1 1 0 1.3.2 2.5.6 3.6.1.3 0 .7-.2 1z"/></svg></span>
    <span class="phone-text">0800 555 019</span>
  </div>
  <div class="abs contact-item" style="left:557px">
    <span class="contact-icon"><svg width="14" height="11" viewBox="0 0 24 18"><rect x="1" y="1" width="22" height="16" rx="2" fill="#fff"/><path d="M2 3l10 7 10-7" stroke="#1b3d6e" stroke-width="2" fill="none"/></svg></span>
    <a class="mail-text" href="#">info@harbourframe.co.nz</a>
  </div>
</header>

<nav class="abs nav">
  <div class="abs nav-active"></div>
  <span class="abs nav-item" style="left:86px">HOME</span>
  <span class="abs nav-item" style="left:144px">GALLERY</span>
  <span class="abs nav-item" style="left:214px">ABOUT US</span>
  <span class="abs nav-item" style="left:290px">MOBILE HOMES</span>
  <span class="abs nav-item" style="left:388px">TESTIMONIALS</span>
  <span class="abs nav-item" style="left:482px">FAQ'S</span>
  <span class="abs nav-item" style="left:539px">USEFUL LINKS</span>
  <span class="abs nav-item" style="left:631px">CONTACT US</span>
</nav>

<section>
  <div class="abs hero" role="img" aria-label="Photo of a white relocatable holiday cabin with a picnic table under trees"></div>
  <h1 class="abs hero-title">RELOCATABLE HOLIDAY HOMES</h1>
  <div class="abs hero-dots"><span></span><span></span><span></span><span></span></div>
</section>

<section>
  <h2 class="abs welcome-title">WELCOME TO HARBOURFRAME</h2>
  <p class="abs welcome-sub">Harbourframe are New Zealands largest manufacturer of trailerised accommodation units</p>
  <div class="abs welcome-copy">
    <p>With over 14 years in the industry and well over 1200 units in place, Harbourframe have a solution to your accommodation requirements. From our 'Sleep Out' units and popular Caravan Annex's, through to the Traveller and Chalet, Harbourframes' range is renowned for quality and reliability. Our design team will work with you to ensure you get the right unit to fit your lifestyle and budget.</p>
    <p>Leisure time is both personal time and extremely precious. Harbourframe can play an important role in a community and way of life that is reflective of increasing awareness and expectations of standards and quality of those leisure times.</p>
  </div>
  <a class="abs read-more" href="#">READ MORE &gt;&gt;</a>
  <svg class="abs badge" width="126" height="126" viewBox="0 0 126 126" role="img" aria-label="Certification badge">
    <circle cx="63" cy="63" r="61" fill="none" stroke="#888" stroke-width="2"/>
    <circle cx="63" cy="63" r="42" fill="#2a2627"/>
  </svg>
</section>

<section class="abs range">
  <h2 class="abs range-title">OUR RANGE</h2>
  <a class="abs range-card" style="left:64px" href="#"><div class="range-photo" style="background:linear-gradient(180deg,#5f9fd8 0%,#a8cdee 35%,#e8e8e4 60%,#7a3b2a 100%)" role="img" aria-label="Photo of a chalet with a timber deck"></div><span class="range-name">CHALET</span><span class="range-more">VIEW RANGE &gt;&gt;</span></a>
  <a class="abs range-card" style="left:173px" href="#"><div class="range-photo" style="background:linear-gradient(180deg,#cfd3d3 0%,#f0eee9 45%,#4d5048 75%,#6f7d4a 100%)" role="img" aria-label="Photo of a duplex unit with a veranda"></div><span class="range-name">DUPLEX</span><span class="range-more">VIEW RANGE &gt;&gt;</span></a>
  <a class="abs range-card" style="left:282px" href="#"><div class="range-photo" style="background:linear-gradient(180deg,#6f8a4c 0%,#c9ccc6 40%,#8a6a4a 75%,#6d8a40 100%)" role="img" aria-label="Photo of a caravan annex with a deck"></div><span class="range-name">ANNEX</span><span class="range-more">VIEW RANGE &gt;&gt;</span></a>
  <a class="abs range-card" style="left:391px" href="#"><div class="range-photo" style="background:linear-gradient(180deg,#6a8a3e 0%,#8ea060 35%,#d6d8d2 60%,#7f9a4a 100%)" role="img" aria-label="Photo of a traveller unit in a holiday park"></div><span class="range-name">TRAVELLER</span><span class="range-more">VIEW RANGE &gt;&gt;</span></a>
  <a class="abs range-card" style="left:500px" href="#"><div class="range-photo" style="background:linear-gradient(180deg,#8fb6dc 0%,#dfe3e4 45%,#b9b3a6 70%,#6d8a48 100%)" role="img" aria-label="Photo of a residential relocatable home"></div><span class="range-name">RESIDENTIAL</span><span class="range-more">VIEW RANGE &gt;&gt;</span></a>
  <a class="abs range-card" style="left:609px" href="#"><div class="range-photo" style="background:linear-gradient(180deg,#9db2c6 0%,#e6e6e2 45%,#7c7c78 72%,#5d6b48 100%)" role="img" aria-label="Photo of a business site office unit"></div><span class="range-name">BUSINESS</span><span class="range-more">VIEW RANGE &gt;&gt;</span></a>
</section>

<section>
  <div class="abs box" style="left:64px;width:207px">
    <h3 class="box-title">CLIENT TESTIMONIALS</h3>
    <p class="quote"><b>&ldquo;</b> At vero eos et accusamus et iusto odio dignissimos ducimus qui blanditiis praesentium voluptatum de leniti atque corrupti quos dolores et quas moles tias excepturi sint occaecati cupiditate non provident <b>&rdquo;</b></p>
    <p class="quote-author"><strong>- SAM CARTER</strong> &nbsp;( Manager )</p>
  </div>
  <div class="abs box" style="left:284px;width:207px">
    <h3 class="box-title">LATEST NEWS</h3>
    <div class="news" style="top:54px"><div class="news-title">NEMO ENIM IPSAM VOLUPTATEM QUIA</div><div class="news-meta"><span>11/12/2015</span><span>09:00</span><span>3 Comments</span></div></div>
    <div class="news" style="top:98px"><div class="news-title">NEMO ENIM IPSAM VOLUPTATEM QUIA</div><div class="news-meta"><span>11/12/2015</span><span>09:00</span><span>3 Comments</span></div></div>
    <div class="news" style="top:143px"><div class="news-title">NEMO ENIM IPSAM VOLUPTATEM QUIA</div><div class="news-meta"><span>11/12/2015</span><span>09:00</span><span>3 Comments</span></div></div>
    <a class="box-link" style="left:15px" href="#">VIEW MORE &gt;&gt;</a>
  </div>
  <div class="abs box" style="left:503px;width:207px">
    <h3 class="box-title">OUR LOCATION</h3>
    <div class="map" role="img" aria-label="Street map showing the office location"></div>
    <a class="box-link" style="left:16px" href="#">VISIT US &gt;&gt;</a>
  </div>
</section>

<footer class="abs footer">
  <h4 class="abs foot-head" style="left:64px">USEFUL LINKS</h4>
  <div class="abs foot-links" style="left:64px"><a href="#">Coastal Parks</a><a href="#">Camping Grounds Network</a><a href="#">Best Stay Parks</a><a href="#">(RHA)</a></div>
  <div class="abs foot-links" style="left:167px"><a href="#">Kauri Grove</a><a href="#">Sandy Point Beach</a><a href="#">Harbour Beach</a><a href="#">Tui Court Motel</a></div>
  <h4 class="abs foot-head" style="left:271px">FAQ</h4>
  <div class="abs foot-links" style="left:271px"><a href="#">What is a 'Bach?</a><a href="#">Will I need a Building Permit?</a><a href="#">Can you build to our specifications?</a><a href="#">How many bedrooms can we have?</a></div>
  <h4 class="abs foot-head" style="left:433px">CONTACT US</h4>
  <div class="abs foot-contact">
    <div><svg width="8" height="10" viewBox="0 0 8 10"><path d="M4 0a4 4 0 0 1 4 4c0 3-4 6-4 6S0 7 0 4a4 4 0 0 1 4-4z" fill="#ddd"/><circle cx="4" cy="4" r="1.4" fill="#242021"/></svg><span>Harbourframe Ltd 48 Kowhai Road<br>Rd2 Tauranga 3172</span></div>
    <div><svg width="9" height="9" viewBox="0 0 24 24"><path fill="#ddd" d="M6.6 10.8a15 15 0 0 0 6.6 6.6l2.2-2.2c.3-.3.7-.4 1-.2 1.1.4 2.3.6 3.6.6.6 0 1 .4 1 1V20c0 .6-.4 1-1 1A17 17 0 0 1 3 4c0-.6.4-1 1-1h3.5c.6 0 1 .4 1 1 0 1.3.2 2.5.6 3.6.1.3 0 .7-.2 1z"/></svg><span>0800 555 019</span></div>
    <div><svg width="6" height="9" viewBox="0 0 6 9"><rect x=".5" y=".5" width="5" height="8" rx="1" fill="none" stroke="#ddd"/></svg><span>021 555 0142</span></div>
    <div><svg width="11" height="8" viewBox="0 0 24 18"><rect x="1" y="1" width="22" height="16" fill="#ddd"/><path d="M2 3l10 7 10-7" stroke="#242021" stroke-width="2" fill="none"/></svg><span>info@harbourframe.co.nz</span></div>
  </div>
  <div class="abs foot-brand"><span class="brand-mark"></span><span class="brand-name">HARBOURFRAME</span></div>
  <p class="abs copyright">Copyright © Harbourframe. All rights reserved.</p>
  <div class="abs social"><span></span><span></span><span></span><span></span></div>
</footer>

</body>
</html>
```